Lumen Forge Unique Marketing Website Design

I am starting a new company that is a thought leader in the marketing consulting space. The company is called Lumen Forge. We intend to build a Wordpress site on the Astra Theme with the Spectra builder. Our goal is to become the leading voice that empowers high-ticket service business leaders to become Lumen Forge by equipping them with the cutting-edge frameworks and decision grade intelligence taught in leading business schools. What we are looking for is a website design that is clean and professional, making some use of white space well also being eye catching and distinctive in the consulting space. We will probably want to have a video on the homepage not in the hero section, but just below to explain the company and what we do. Our tagline is "Be found. Be chosen." I have attached a brand guide with some messaging, our typography choices, and our color system. The full site will have a primary nav that is four pages - About us, Services, Insights (essentially a blog), and Contact Us. The goal of this project is to develop an art direction that I can give to a designer to build loads of new pages.

Target Market(s)

Business owners (mostly male) from 30-60 years old, looking to fix their sales and marketing funnel.

Industry/Entity Type

Marketing consulting

Font styles to use
Sans Serif

Requirements
Must have
• A clean, professional design that builds trust with owners of high-ticket service businesses. We need a space for explainer video, and sections that tell prospects what we do. Would also like to have a blog carousel.
Nice to have
• Social feeds, if possible. See attached documents for colors and fonts.
Should not have
• Our feel is professional enough to be trustworthy, but unique enough to be memorable. Cartoon ideas do not meet the professional test, and we do not want the website to appear feminine.

```html
<!DOCTYPE html>
<html lang="en">
<head>
<meta charset="utf-8">
<title>Lumen Forge — Marketing Consulting</title>
<link href="https://fonts.googleapis.com/css2?family=Oswald:wght@500;600;700&family=Poppins:wght@400;500;600;700&display=swap" rel="stylesheet">
<style>
:root{
  --blue:#2d57e8;
  --blue-soft:#e9eefc;
  --ink:#151a22;
  --text:#5b6170;
  --muted:#8c909a;
  --line:#e3e6ec;
  --grey-bg:#f3f4f6;
  --dark:#3a3b3d;
  --navy:#0e1a38;
  --navy-deep:#09122a;
  --accent:#e2483a;
  --white:#ffffff;
}
*{box-sizing:border-box;margin:0;padding:0}
html,body{width:1200px;height:4224px;overflow:hidden}
body{font-family:"Poppins",Arial,sans-serif;color:var(--text);background:var(--white);position:relative;font-size:13px;line-height:1.6}
.h-display{font-family:"Oswald","Arial Narrow",sans-serif;font-weight:700;text-transform:uppercase;color:var(--ink);letter-spacing:.5px}
.h-display .accent{color:var(--blue)}
.h-display .bar{display:inline-block;width:3px;height:.85em;background:currentColor;margin:0 10px;vertical-align:-2px}
.btn{display:inline-block;font-family:"Poppins",Arial,sans-serif;font-weight:600;font-size:11px;letter-spacing:.6px;text-transform:uppercase;color:var(--white);background:var(--ink);padding:11px 22px;border-radius:4px}
.ph{display:block}

/* header */
.site-header{position:absolute;top:0;left:0;width:1200px;height:72px;background:var(--white);display:flex;align-items:center;padding:0 72px;justify-content:space-between;z-index:2}
.brand{display:flex;align-items:center;gap:10px;font-family:"Oswald","Arial Narrow",sans-serif;font-weight:700;font-size:27px;color:var(--ink);text-transform:uppercase;letter-spacing:.5px}
.brand-square{width:14px;height:14px;background:var(--blue)}
.main-nav{display:flex;align-items:center;gap:34px;font-size:13px;color:var(--ink)}
.main-nav .active{color:var(--blue);border-bottom:2px solid var(--blue);padding-bottom:2px}
.main-nav .btn{margin-left:10px}

/* hero */
.hero{position:absolute;top:72px;left:0;width:1200px;height:490px;background:linear-gradient(120deg,#1b2433 0%,#2d3a4d 45%,#1a222f 100%);text-align:center;padding-top:120px}
.hero-shade{position:absolute;inset:0;background:radial-gradient(ellipse at 50% 45%,rgba(40,52,70,.2),rgba(8,12,20,.55))}
.hero-inner{position:relative}
.hero-tag{font-family:"Poppins",Arial,sans-serif;font-style:italic;font-weight:500;color:var(--accent);font-size:17px;margin-bottom:8px}
.hero-title{font-family:"Oswald","Arial Narrow",sans-serif;font-weight:700;color:var(--white);font-size:62px;line-height:1.08;text-transform:uppercase;letter-spacing:1px}
.hero .btn{margin-top:26px;background:#2b2f36}

/* about */
.about{position:absolute;top:562px;left:0;width:1200px;height:526px}
.about-photo{position:absolute;left:200px;top:78px;width:340px;height:370px;border-radius:8px;background:linear-gradient(160deg,#c9ccd3,#8e96a4 60%,#5f6878)}
.about-body{position:absolute;left:636px;top:100px;width:390px}
.about-body .h-display{font-size:38px;margin-bottom:14px}
.about-body p{font-size:11.5px;margin-bottom:12px;line-height:1.7}
.about-meta{display:flex;gap:40px;margin:18px 0 24px}
.meta-item{display:flex;gap:10px;align-items:center}
.meta-icon{width:36px;height:36px;border-radius:50%;background:var(--blue);display:flex;align-items:center;justify-content:center}
.meta-item small{display:block;font-size:10px;color:var(--muted);line-height:1.3}
.meta-item strong{display:block;font-size:11.5px;color:var(--ink);font-weight:600;line-height:1.3}

/* pillars */
.pillars{position:absolute;top:1088px;left:0;width:1200px;height:974px;background:var(--grey-bg)}
.pillars-head{text-align:center;padding-top:76px}
.pillars-head .h-display{font-size:38px}
.pillars-head p{font-size:12px;color:var(--ink);margin-top:2px}
.pillar-table{position:absolute;left:200px;top:168px;width:800px}
.pillar-cols{display:flex;justify-content:space-between;padding:0 20px 10px}
.pillar-cols div{font-family:"Oswald","Arial Narrow",sans-serif;font-size:13px;color:var(--ink);line-height:1.1}
.pillar-cols div:last-child{width:330px}
.pillar-cols span{display:block;font-size:26px;color:var(--blue);font-weight:600}
.pillar-rows{background:var(--white);border-radius:6px;box-shadow:0 4px 18px rgba(0,0,0,.05)}
.pillar-row{display:grid;grid-template-columns:1fr 90px 1fr;align-items:center;padding:16px 20px;border-bottom:1px solid var(--line)}
.pillar-row:last-child{border-bottom:0}
.cell h4{font-size:9.5px;text-transform:uppercase;color:var(--blue);font-weight:600;letter-spacing:.5px}
.cell p{font-size:11px;color:var(--ink);line-height:1.45}
.row-icon{width:54px;height:54px;margin:0 auto;border-radius:50%;border:1.5px solid var(--blue);display:flex;align-items:center;justify-content:center;background:var(--white)}
.together{position:absolute;left:200px;top:620px;width:420px}
.together .h-display{font-size:28px;color:var(--blue);line-height:1.15;margin-bottom:14px}
.together p{font-size:11px;color:var(--ink);line-height:1.55}
.together ul{list-style:none;margin-top:10px}
.together li{display:flex;gap:8px;margin-bottom:8px;font-size:11px;color:var(--ink);line-height:1.45}
.together li b{font-weight:600;display:block}
.dot{width:8px;height:8px;border-radius:50%;background:var(--blue);margin-top:5px;flex:none}
.together-photo{position:absolute;left:682px;top:580px;width:320px;height:330px;border-radius:6px;background:linear-gradient(150deg,#6d7585,#3d4452 55%,#232834)}

/* different */
.different{position:absolute;top:2062px;left:0;width:1200px;height:578px}
.different-head{text-align:center;padding-top:110px}
.different-head .h-display{font-size:38px}
.different-head p{font-size:12px;color:var(--ink)}
.diff-photo{position:absolute;left:160px;top:190px;width:420px;height:276px;border-radius:8px;background:linear-gradient(135deg,#2b4a7a,#17294a 50%,#0c1628)}
.diff-body{position:absolute;left:644px;top:206px;width:380px}
.check-list{list-style:none}
.check-list li{display:flex;align-items:center;gap:10px;font-size:11.5px;color:var(--ink);margin-bottom:12px}
.check{width:14px;height:14px;border-radius:3px;background:var(--blue);flex:none;display:flex;align-items:center;justify-content:center}
.diff-body h5{font-size:11px;font-weight:700;color:var(--ink);text-transform:uppercase;line-height:1.5;margin:14px 0 6px}
.diff-body p{font-size:11px;color:var(--ink);line-height:1.55;margin-bottom:18px}

/* credentials */
.credentials{position:absolute;top:2640px;left:0;width:1200px;height:560px;background:var(--dark)}
.credentials .h-display{text-align:center;color:var(--white);font-size:40px;padding-top:142px}
.cred-grid{position:absolute;left:220px;top:220px;width:760px;display:grid;grid-template-columns:repeat(4,1fr);gap:30px;text-align:center}
.cred-icon{width:70px;height:70px;margin:0 auto 12px;border-radius:50%;background:var(--white);display:flex;align-items:center;justify-content:center}
.cred-grid p{font-size:11px;color:var(--white);line-height:1.45}
.video{position:absolute;left:232px;top:3060px;width:736px;height:272px;border-radius:6px;background:linear-gradient(120deg,#2f3b52,#1e2636 55%,#121722);overflow:hidden}
.video-play{position:absolute;left:568px;top:3166px;width:60px;height:60px;border-radius:50%;background:var(--blue);display:flex;align-items:center;justify-content:center;box-shadow:0 0 0 10px rgba(45,87,232,.3)}

/* blog */
.blog{position:absolute;top:3332px;left:0;width:1200px;height:528px}
.blog .h-display{text-align:center;font-size:40px;padding-top:80px}
.blog-cards{position:absolute;left:232px;top:140px;width:736px;display:grid;grid-template-columns:1fr 1fr;gap:32px}
.blog-img{height:190px;border-radius:6px}
.blog-img.one{background:linear-gradient(135deg,#c6b48d,#7c7f86)}
.blog-img.two{background:linear-gradient(135deg,#9aa6bb,#4c5568)}
.blog-meta{display:flex;align-items:center;gap:8px;font-size:10px;color:var(--blue);font-weight:600;margin:14px 0 4px}
.blog-meta i{width:18px;height:18px;border-radius:50%;background:var(--blue);display:block}
.blog-card p{font-size:11px;color:var(--ink);line-height:1.5}
.arrow{position:absolute;top:240px;width:20px;height:20px;display:flex;align-items:center;justify-content:center}
.arrow.left{left:196px}.arrow.right{left:984px}
.blog .btn{position:absolute;left:560px;top:442px;padding:9px 18px}

/* footer */
.site-footer{position:absolute;top:3860px;left:0;width:1200px;height:320px;background:var(--navy)}
.footer-brand{display:flex;justify-content:center;padding-top:40px}
.footer-brand .brand{color:var(--white);font-size:34px}
.footer-cols{position:absolute;top:124px;left:152px;width:896px;display:grid;grid-template-columns:180px 150px 250px 1fr;gap:30px}
.footer-cols h6{font-size:11px;font-weight:600;color:var(--blue);text-transform:uppercase;margin-bottom:10px;letter-spacing:.4px}
.footer-cols li{list-style:none;font-size:10.5px;color:#cfd4e0;margin-bottom:7px;display:flex;gap:7px;align-items:flex-start;line-height:1.4}
.f-dot{width:10px;height:10px;border-radius:50%;background:var(--blue);flex:none;margin-top:3px}
.newsletter{display:flex;margin-bottom:14px}
.newsletter span{flex:1;background:var(--white);font-size:10px;color:var(--muted);padding:8px 10px;border-radius:3px 0 0 3px}
.newsletter b{width:36px;background:var(--blue);border-radius:0 3px 3px 0;display:flex;align-items:center;justify-content:center}
.map{height:130px;border-radius:4px;background:linear-gradient(135deg,#e6e8ec,#cfd5de)}
.footer-bar{position:absolute;top:4180px;left:0;width:1200px;height:44px;background:var(--navy-deep);display:flex;align-items:center;justify-content:space-between;padding:0 52px;font-size:10px;color:#aab1c2}
.socials{display:flex;gap:8px}
.socials i{width:20px;height:20px;border-radius:50%;background:#2b3656;display:block}
</style>
</head>
<body>

<header class="site-header">
  <div class="brand"><span>Lumen Forge</span><span class="brand-square"></span></div>
  <nav class="main-nav">
    <span class="active">Home</span><span>About Us</span><span>Services</span><span>Blog</span><span>Contact Us</span>
    <span class="btn">Let's Get In Touch</span>
  </nav>
</header>

<section class="hero" role="img" aria-label="Dark photo of a business team meeting in a modern office">
  <div class="hero-shade"></div>
  <div class="hero-inner">
    <p class="hero-tag">Be Found. Be Chosen.</p>
    <h1 class="hero-title">We Provide<br>Business Solutions</h1>
    <span class="btn">Consult Now</span>
  </div>
</section>

<section class="about">
  <div class="about-photo ph" role="img" aria-label="Photo of a smiling consultant at a desk"></div>
  <div class="about-body">
    <h2 class="h-display">About<span class="bar"></span><span class="accent">Us</span></h2>
    <p>We help owners of high-ticket service firms fix the way buyers find them, trust them and choose them. Our work joins clear research with sharp messaging so every stage of the funnel pulls its weight and wins better clients.</p>
    <p>Each plan we build starts with how your customer thinks and ends with a system your team can run, measure and improve week after week.</p>
    <div class="about-meta">
      <div class="meta-item">
        <span class="meta-icon"><svg width="16" height="16" viewBox="0 0 24 24" fill="#fff"><path d="M6.6 10.8a15.1 15.1 0 0 0 6.6 6.6l2.2-2.2c.3-.3.7-.4 1-.2 1.1.4 2.3.6 3.6.6.6 0 1 .4 1 1V20c0 .6-.4 1-1 1A17 17 0 0 1 3 4c0-.6.4-1 1-1h3.5c.6 0 1 .4 1 1 0 1.3.2 2.5.6 3.6.1.3 0 .7-.2 1z"/></svg></span>
        <div><small>Call Us</small><strong>(555) 010-2040</strong></div>
      </div>
      <div class="meta-item">
        <span class="meta-icon"><svg width="16" height="16" viewBox="0 0 24 24" fill="none" stroke="#fff" stroke-width="2"><circle cx="12" cy="12" r="9"/><path d="M12 7v5l3 2"/></svg></span>
        <div><small>Sat - Fri</small><strong>7:00am-7:00pm</strong></div>
      </div>
    </div>
    <span class="btn">Read More</span>
  </div>
</section>

<section class="pillars">
  <div class="pillars-head">
    <h2 class="h-display">The Two<span class="bar"></span><span class="accent">Pillars</span></h2>
    <p>Lumen Forge Methodology Rests On Two Complementary Disciplines.</p>
  </div>
  <div class="pillar-table">
    <div class="pillar-cols">
      <div>Buyer<span>INSIGHT</span></div>
      <div>Choice<span>DESIGN</span></div>
    </div>
    <div class="pillar-rows">
      <div class="pillar-row">
        <div class="cell"><h4>Definition</h4><p>The Discipline Of Uncovering And Diagnosing What Is Actually Happening In A Buyer's Journey Before Prescribing Solutions.</p></div>
        <div class="row-icon"><svg width="24" height="24" viewBox="0 0 24 24" fill="none" stroke="#2d57e8" stroke-width="1.8"><rect x="5" y="3" width="14" height="18" rx="2"/><path d="M9 8h6M9 12h6M9 16h4"/></svg></div>
        <div class="cell"><h4>Definition</h4><p>The Discipline Of Applying Behavioral Science Principles To Design Buying Experiences Where Saying Yes Feels Safer Than Saying No.</p></div>
      </div>
      <div class="pillar-row">
        <div class="cell"><h4>Metaphor</h4><p>Reconnaissance. Gathering Intel On The Battlefield Before Making Strategic Decisions.</p></div>
        <div class="row-icon"><svg width="24" height="24" viewBox="0 0 24 24" fill="none" stroke="#2d57e8" stroke-width="1.8"><circle cx="12" cy="12" r="8"/><circle cx="12" cy="12" r="3"/><path d="M12 2v4M12 18v4M2 12h4M18 12h4"/></svg></div>
        <div class="cell"><h4>Metaphor</h4><p>Decision Architecture. Engineering The Environment In Which High-Stakes Choices Get Made.</p></div>
      </div>
      <div class="pillar-row">
        <div class="cell"><h4>Output</h4><p>A Diagnosis. A Clear-Eyed Assessment Of Reality, Not Assumptions.</p></div>
        <div class="row-icon"><svg width="24" height="24" viewBox="0 0 24 24" fill="none" stroke="#2d57e8" stroke-width="1.8"><path d="M4 20V10M10 20V4M16 20v-7M22 20H2"/></svg></div>
        <div class="cell"><h4>Output</h4><p>A Design System. Principles And Architecture For What To Build, Not Just Tactics To Try.</p></div>
      </div>
    </div>
  </div>

  <div class="together">
    <h3 class="h-display">How The Two Pillars<br>Work Together</h3>
    <p>Buyer Insight Tells You What's True. Choice Design Tells You What To Do About It.</p>
    <p style="margin-top:10px">A Company Might Need:</p>
    <ul>
      <li><span class="dot"></span><span><b>Just Insight:</b>We don't know why deals stall. Give us the answer.</span></li>
      <li><span class="dot"></span><span><b>Just Design:</b>We understand our problem. Teach us the principles to redesign.</span></li>
      <li><span class="dot"></span><span><b>Both:</b>Diagnose us, then show us what to build.</span></li>
    </ul>
  </div>
  <div class="together-photo ph" role="img" aria-label="Photo of two consultants reviewing notes at a meeting table"></div>
</section>

<section class="different">
  <div class="different-head">
    <h2 class="h-display">What Makes Lumen Forge<span class="bar"></span><span class="accent">Different</span></h2>
    <p>Most Consultants Sell Tactics. We Focus On One Slice Of The Revenue Problem.</p>
  </div>
  <div class="diff-photo ph" role="img" aria-label="Photo of a hand choosing between yes, no and maybe on a digital screen"></div>
  <div class="diff-body">
    <ul class="check-list">
      <li><span class="check"><svg width="9" height="9" viewBox="0 0 12 12" fill="none" stroke="#fff" stroke-width="2"><path d="M2 6l3 3 5-6"/></svg></span>Marketing consultants focus on awareness and lead generation</li>
      <li><span class="check"><svg width="9" height="9" viewBox="0 0 12 12" fill="none" stroke="#fff" stroke-width="2"><path d="M2 6l3 3 5-6"/></svg></span>Sales enablement focuses on closing</li>
      <li><span class="check"><svg width="9" height="9" viewBox="0 0 12 12" fill="none" stroke="#fff" stroke-width="2"><path d="M2 6l3 3 5-6"/></svg></span>Customer success focuses on retention</li>
    </ul>
    <h5>Lumen Forge looks at the entire customer journey through the eyes of the customer.</h5>
    <p>As distinct from the company's journey with the customer. To find the hidden leaks, Lumen Forge applies tested frameworks, methodologies and systems taught in leading business schools to every stage of the funnel.</p>
    <span class="btn">Consult Now</span>
  </div>
</section>

<section class="credentials">
  <h2 class="h-display">Founder<span class="bar"></span><span class="accent">Credentials</span></h2>
  <div class="cred-grid">
    <div><div class="cred-icon"><svg width="30" height="30" viewBox="0 0 24 24" fill="none" stroke="#2d57e8" stroke-width="1.6"><path d="M2 9l10-5 10 5-10 5z"/><path d="M6 11v5c3 2 9 2 12 0v-5"/></svg></div><p>Global Background<br>With Grounded<br>Credibility</p></div>
    <div><div class="cred-icon"><svg width="30" height="30" viewBox="0 0 24 24" fill="none" stroke="#2d57e8" stroke-width="1.6"><circle cx="12" cy="8" r="4"/><path d="M4 21c1-4 4-6 8-6s7 2 8 6"/></svg></div><p>Seasoned Marketing<br>Professor Who Trains<br>Top-Tier Strategy<br>Consultants</p></div>
    <div><div class="cred-icon"><svg width="30" height="30" viewBox="0 0 24 24" fill="none" stroke="#2d57e8" stroke-width="1.6"><path d="M4 20V12M10 20V8M16 20V4M22 20H2"/></svg></div><p>$20M+ In Net Sales<br>Achieved Using These<br>Methods</p></div>
    <div><div class="cred-icon"><svg width="30" height="30" viewBox="0 0 24 24" fill="none" stroke="#2d57e8" stroke-width="1.6"><rect x="4" y="3" width="16" height="18" rx="2"/><path d="M8 8h8M8 12h8M8 16h5"/></svg></div><p>Unique Skill In Making<br>Formal, MBA-Level<br>Frameworks Accessible To<br>Mid-Market Businesses</p></div>
  </div>
</section>

<div class="video ph" role="img" aria-label="Explainer video still of a team meeting around a laptop"></div>
<div class="video-play"><svg width="20" height="20" viewBox="0 0 24 24" fill="#fff"><path d="M8 5v14l11-7z"/></svg></div>

<section class="blog">
  <h2 class="h-display">Our<span class="bar"></span><span class="accent">Blog</span></h2>
  <span class="arrow left"><svg width="14" height="14" viewBox="0 0 24 24" fill="none" stroke="#151a22" stroke-width="2.5"><path d="M15 4l-8 8 8 8"/></svg></span>
  <span class="arrow right"><svg width="14" height="14" viewBox="0 0 24 24" fill="none" stroke="#151a22" stroke-width="2.5"><path d="M9 4l8 8-8 8"/></svg></span>
  <div class="blog-cards">
    <article class="blog-card">
      <div class="blog-img one ph" role="img" aria-label="Photo of colleagues talking in a bright office"></div>
      <div class="blog-meta"><i></i>Jan 18, 2026</div>
      <p>Why Buyers Stall Before They Sign, And The Simple Questions That Help You Find Out Where.</p>
    </article>
    <article class="blog-card">
      <div class="blog-img two ph" role="img" aria-label="Photo of a team gathered around a laptop"></div>
      <div class="blog-meta"><i></i>Jan 18, 2026</div>
      <p>Designing A Sales Path Where Saying Yes Feels Safer Than Waiting For A Better Offer.</p>
    </article>
  </div>
  <span class="btn">View All</span>
</section>

<footer class="site-footer">
  <div class="footer-brand"><div class="brand"><span>Lumen Forge</span></div></div>
  <div class="footer-cols">
    <div>
      <h6>Contact Us</h6>
      <ul>
        <li><span class="f-dot"></span>(555) 010-2040</li>
        <li><span class="f-dot"></span>(555) 010-2041</li>
        <li><span class="f-dot"></span>hello@lumenforge.co</li>
        <li><span class="f-dot"></span>48 Harbor Row, Suite 12, Fairview</li>
      </ul>
    </div>
    <div>
      <h6>Quick Links</h6>
      <ul><li>Home</li><li>About Us</li><li>Services</li><li>Blog</li><li>Contact Us</li></ul>
    </div>
    <div>
      <h6>Subscribe To Our<br>Newsletter</h6>
      <div class="newsletter"><span>Enter your email</span><b><svg width="12" height="12" viewBox="0 0 24 24" fill="#fff"><path d="M2 21l21-9L2 3v7l15 2-15 2z"/></svg></b></div>
      <h6>Opening Hours</h6>
      <ul><li>Mon - Fri: 9:00 am - 6:00 pm</li><li>Sat - Sun: 10:00 am - 2:00 pm</li></ul>
    </div>
    <div class="map ph" role="img" aria-label="Map showing the office location"></div>
  </div>
</footer>
<div class="footer-bar">
  <span>© 2026 Lumen Forge. All Rights Reserved.</span>
  <span class="socials"><i></i><i></i><i></i></span>
</div>

</body>
</html>
```